Peanut Butter - Single Serve Sachet

We are a sports and wellness nutrition company (https://www.brimleyfuel.in) and launching a new product Peanut Butter. Need attractive design of single serve sachet.

The product should be unique and eye catchy. It should have enough space to mention USPs later.

The product USP is tear-on the go sachet, image mockup has been attached.

Target Market(s)

Sports Persons and General Public looking for Peanut Butter.

Industry/Entity Type

Nutrition

Colors

Designer to choose colors to be used in the design.

Requirements
Must have
• Single serve sachet design. Attractive colour theme with Peanut Butter mentioned as bold.
Should not have
• no black colour

```html
<!DOCTYPE html>
<html lang="en">
<head>
<meta charset="utf-8">
<title>Brimley Fuel – Peanut Butter Sachet</title>
<link href="https://fonts.googleapis.com/css2?family=Alfa+Slab+One&family=Montserrat:wght@400;600&family=Lobster+Two:ital,wght@1,700&display=swap" rel="stylesheet">
<style>
  :root {
    --backdrop: #3a3a3c;
    --panel: #ffffff;
    --brand-blue: #0e72bb;
    --title-blue: #1570c0;
    --leaf-green: #a3c466;
    --leaf-green-deep: #88a95a;
    --foil-light: #f2f3f5;
    --foil-mid: #c9ccd1;
    --spread-light: #e9a86a;
    --spread-dark: #b0602e;
    --shell: #d9a765;
    --text-light: #ffffff;
  }
  html, body {
    margin: 0;
    padding: 0;
    width: 1200px;
    height: 2190px;
    overflow: hidden;
    background: var(--backdrop);
  }
  .sachet {
    position: absolute;
    left: 135px;
    top: 136px;
    width: 930px;
    height: 1917px;
    background: var(--panel);
    overflow: hidden;
  }
  .sachet-art {
    position: absolute;
    inset: 0;
    width: 930px;
    height: 1917px;
  }
  .brand {
    position: absolute;
    left: 0;
    width: 930px;
    top: 592px;
    text-align: center;
    color: var(--text-light);
    font-family: "Montserrat", sans-serif;
  }
  .brand-mark {
    display: inline-block;
    width: 24px;
    height: 24px;
    border-radius: 50%;
    background: var(--text-light);
    vertical-align: middle;
    margin-right: 16px;
  }
  .brand-name {
    font-weight: 600;
    font-size: 52px;
    line-height: 60px;
    letter-spacing: 1px;
    vertical-align: middle;
  }
  .brand-rule {
    width: 565px;
    height: 2px;
    background: var(--text-light);
    margin: 2px auto 6px;
    opacity: 0.8;
  }
  .brand-tagline {
    font-weight: 400;
    font-size: 20px;
    letter-spacing: 6px;
  }
  .product-title {
    position: absolute;
    left: 0;
    top: 0;
    width: 930px;
    margin: 0;
    color: var(--title-blue);
    font-family: "Alfa Slab One", serif;
    font-weight: 400;
  }
  .product-title .line-large {
    position: absolute;
    left: 203px;
    top: 898px;
    font-size: 174px;
    line-height: 1;
    letter-spacing: -4px;
  }
  .product-title .line-small {
    position: absolute;
    left: 392px;
    top: 838px;
    font-size: 102px;
    line-height: 1;
    letter-spacing: -1px;
  }
  .product-visual {
    position: absolute;
    left: 148px;
    top: 1140px;
    width: 723px;
    height: 330px;
  }
  .product-blurb {
    position: absolute;
    left: 186px;
    top: 1424px;
    margin: 0;
    width: 480px;
    color: var(--text-light);
    font-family: "Lobster Two", cursive;
    font-style: italic;
    font-weight: 700;
    font-size: 30px;
    line-height: 36px;
  }
</style>
</head>
<body>
  <main class="sachet">
    <svg class="sachet-art" viewBox="0 0 930 1917" aria-hidden="true">
      <defs>
        <linearGradient id="foil" x1="0" y1="0" x2="1" y2="0">
          <stop offset="0" stop-color="var(--foil-mid)"/>
          <stop offset="0.2" stop-color="var(--foil-light)"/>
          <stop offset="0.5" stop-color="#dcdfe3"/>
          <stop offset="0.8" stop-color="var(--foil-light)"/>
          <stop offset="1" stop-color="var(--foil-mid)"/>
        </linearGradient>
        <clipPath id="pouch-clip">
          <path d="M325,50 L612,50 Q652,50 652,90 L652,330 Q652,380 700,410 L830,500 Q871,530 871,580 L871,1720 Q871,1780 811,1780 L120,1780 Q60,1780 60,1720 L60,580 Q60,530 101,500 L231,410 Q285,380 285,330 L285,90 Q285,50 325,50 Z"/>
        </clipPath>
      </defs>
      <path class="base-wave" d="M0,1212 C380,1150 800,1300 930,1760 L930,1917 L0,1917 Z" fill="var(--leaf-green)"/>
      <path class="pouch" d="M325,50 L612,50 Q652,50 652,90 L652,330 Q652,380 700,410 L830,500 Q871,530 871,580 L871,1720 Q871,1780 811,1780 L120,1780 Q60,1780 60,1720 L60,580 Q60,530 101,500 L231,410 Q285,380 285,330 L285,90 Q285,50 325,50 Z" fill="url(#foil)"/>
      <path class="pouch-wave" clip-path="url(#pouch-clip)" d="M0,1212 C380,1150 800,1300 930,1760 L930,1917 L0,1917 Z" fill="var(--leaf-green-deep)" opacity="0.95"/>
      <path class="crown" d="M0,0 L930,0 L930,362 A465,441 0 0 1 0,362 Z" fill="var(--brand-blue)" opacity="0.97"/>
      <path class="pouch-ghost" clip-path="url(#pouch-clip)" d="M0,0 L930,0 L930,362 A465,441 0 0 1 0,362 Z" fill="#ffffff" opacity="0.05"/>
    </svg>

    <div class="brand">
      <span class="brand-mark"></span><span class="brand-name">Brimley Fuel</span>
      <div class="brand-rule"></div>
      <div class="brand-tagline">PREMIUM SPORTS NUTRITION</div>
    </div>

    <h1 class="product-title">
      <span class="line-large">Butter</span>
      <span class="line-small">peanut</span>
    </h1>

    <svg class="product-visual" viewBox="0 0 723 330" role="img" aria-label="Peanuts in their shells beside a glass jar of creamy peanut butter with a spoon">
      <defs>
        <radialGradient id="spread" cx="0.55" cy="0.4" r="0.6">
          <stop offset="0" stop-color="var(--spread-light)"/>
          <stop offset="1" stop-color="var(--spread-dark)"/>
        </radialGradient>
      </defs>
      <ellipse cx="170" cy="120" rx="165" ry="100" fill="var(--shell)"/>
      <ellipse cx="545" cy="160" rx="175" ry="165" fill="url(#spread)"/>
    </svg>

    <p class="product-blurb">Lorem ipsum dolor<br>sit amet, consectetuer<br>adipiscing elit, sed<br>diam nonummy nibh<br>euismod tincidunt ut laoreet dolore<br>magna aliquam erat volutpat.</p>
  </main>
</body>
</html>
```